Fun relaxed Travel Photography Business Card*

Require a fun, funky and quirky but rememberable business card for a travel photographer

Industry/Entity Type

Photographer

Contact Information for Business Card

Front Card

(my name) Tavo M.

Travel Photographer ( small under travel photographer) “self-proclaimed”

(website logo) wanderingtavo.example

(plain square marker logo) @wandering_with_tavo

(plain square marker logo) @wandering_with_tavo_2.0 (backup for when plain square marker puts Tavo on timeout for bad behaviour)

Tel: N/A (removing the potential awkwardness of me not replying)

Email: (see above)

Back Card

Offending people since 1986

(Bottom right corner) “p.s. travelling made me fatTER”

Font styles to use
Serif

Colors

Designer to choose colors to be used in the design.

Requirements
Must have
• a camera
• a similar cartoon version of me as the "logo" see attached files, try to make as similar as possible

```html
<!DOCTYPE html>
<html lang="en">
<head>
<meta charset="utf-8">
<title>Tavo M. – Travel Photographer Business Card</title>
<link rel="stylesheet" href="https://fonts.googleapis.com/css2?family=Roboto+Slab:wght@400;700&family=Zilla+Slab:ital,wght@1,400;0,700&display=swap">
<style>
  :root{
    --backdrop:#2a2c30;
    --card:#ffffff;
    --ink:#1d1a22;
    --ink-soft:#3a3446;
    --splash-yellow:#f9c93c;
    --splash-orange:#f6843a;
    --splash-pink:#ee4f8f;
    --splash-purple:#7b4fc9;
    --splash-blue:#2f67d8;
    --splash-teal:#22b6c2;
    --splash-green:#7ccf3a;
    --photo-frame:#ffffff;
    --avatar-fill:#3a5bb0;
    --globe:#f2a31b;
    --handle-mark:#e2456f;
  }
  *{box-sizing:border-box;margin:0;padding:0}
  html,body{width:1200px;height:900px;overflow:hidden}
  body{background:var(--backdrop);position:relative;font-family:"Roboto Slab",Georgia,serif;color:var(--ink)}

  .card{position:absolute;left:250px;width:700px;height:400px;background:var(--card);border-radius:26px;overflow:hidden;box-shadow:0 10px 28px rgba(0,0,0,.45)}
  .card--front{top:30px}
  .card--back{top:470px}

  .splash{position:absolute;border-radius:60px;opacity:.85;
    background:linear-gradient(115deg,var(--splash-yellow),var(--splash-orange) 18%,var(--splash-pink) 34%,var(--splash-purple) 50%,var(--splash-blue) 64%,var(--splash-teal) 80%,var(--splash-green))}
  .card--front .splash{left:60px;top:30px;right:60px;bottom:80px}
  .card--back .splash{left:50px;top:40px;right:50px;bottom:90px}

  /* front */
  .avatar{position:absolute;left:430px;top:20px;width:92px;height:92px;border-radius:50%;border:3px solid #e6e6e6;background:var(--avatar-fill)}
  .name{position:absolute;left:291px;top:116px;width:370px;text-align:center;font-weight:700;font-size:36px;line-height:42px;letter-spacing:1px;color:#fff;text-shadow:0 2px 3px rgba(60,20,60,.6)}
  .role{position:absolute;left:291px;top:160px;width:370px;text-align:center;font-size:26px;line-height:32px;color:#fff;text-shadow:0 1px 3px rgba(60,20,60,.7)}
  .role__aside{position:absolute;left:291px;top:194px;width:370px;text-align:center;font-family:"Zilla Slab",Georgia,serif;font-style:italic;font-size:16px;line-height:20px;color:var(--ink-soft)}
  .photo{position:absolute;width:110px;height:76px;border:4px solid var(--photo-frame);box-shadow:0 3px 8px rgba(0,0,0,.35)}
  .photo--night{left:190px;top:216px;transform:rotate(-4deg);background:#5a2048}
  .photo--beach{left:300px;top:230px;transform:rotate(4deg);background:#3f93c8}
  .photo--camera{left:410px;top:244px;transform:rotate(-3deg);background:#4a4040}
  .photo--city{left:520px;top:256px;transform:rotate(4deg);background:#8a8a4a}
  .handle{position:absolute;left:24px;top:176px;display:flex;align-items:center;gap:8px;font-size:15px;line-height:20px;color:var(--ink)}
  .handle__mark{width:16px;height:16px;border-radius:4px;background:var(--handle-mark)}
  .website{position:absolute;right:78px;bottom:28px;font-size:19px;line-height:24px;color:var(--ink)}
  .globe{position:absolute;right:26px;bottom:24px;width:32px;height:32px}

  /* back */
  .tagline{position:absolute;left:0;top:164px;width:700px;text-align:center;font-size:44px;line-height:54px;color:#fff;text-shadow:0 2px 4px rgba(40,20,60,.55)}
  .postscript{position:absolute;right:24px;bottom:20px;text-align:right;font-weight:700;font-size:17px;line-height:1.2;color:var(--ink)}
</style>
</head>
<body>

<section class="card card--front" aria-label="Business card front">
  <div class="splash" role="img" aria-label="Colourful watercolour paint splash artwork"></div>

  <div class="avatar" role="img" aria-label="Cartoon portrait logo of Tavo"></div>
  <h1 class="name">TAVO M.</h1>
  <p class="role">Travel Photographer</p>
  <p class="role__aside">“self-proclaimed”</p>

  <div class="photo photo--night" role="img" aria-label="Travel photo: night scene"></div>
  <div class="photo photo--beach" role="img" aria-label="Travel photo: palm beach"></div>
  <div class="photo photo--camera" role="img" aria-label="Travel photo: photographer with camera"></div>
  <div class="photo photo--city" role="img" aria-label="Travel photo: hillside town"></div>

  <p class="handle"><span class="handle__mark"></span>@wandering_with_tavo</p>
  <p class="website">wanderingtavo.example</p>
  <svg class="globe" viewBox="0 0 34 34" aria-hidden="true">
    <circle cx="17" cy="17" r="15" fill="var(--globe)"/>
    <g fill="none" stroke="#fff" stroke-width="1.6">
      <ellipse cx="17" cy="17" rx="6.5" ry="15"/>
      <line x1="2" y1="17" x2="32" y2="17"/>
      <line x1="5" y1="9" x2="29" y2="9"/>
      <line x1="5" y1="25" x2="29" y2="25"/>
    </g>
  </svg>
</section>

<section class="card card--back" aria-label="Business card back">
  <div class="splash" role="img" aria-label="Colourful watercolour paint splash artwork"></div>
  <p class="tagline">Offending people since 1986</p>
  <p class="postscript">p.s. Travelling<br>made me fatTER</p>
</section>

</body>
</html>
```